Quarry Vale Business Cards

We need to design some upbeat business cards. We are an Industrial Rope Access Company/Height Safety Company that specialize in Rope Access, Confined Space, Anchor Points, Safety Systems, PPE Inspecions and Rigging.
Company name is Quarry Vale Ltd
Card is for Reggie Stanton the Company Director
His mobile number is 027 816 4920 and email is reggie@quarryvale.co.nz. Website address is www.quarryvale.co.nz.
We will post some pictures below to ensure you get a good idea of what we do.

```html
<!DOCTYPE html>
<html lang="en">
<head>
<meta charset="utf-8">
<title>Quarry Vale Business Cards</title>
<link rel="stylesheet" href="https://fonts.googleapis.com/css2?family=Oxanium:wght@600;700&family=Open+Sans:wght@400;600&display=swap">
<style>
  :root {
    --backdrop: #b9b9b9;
    --navy-deep: #0c2a63;
    --navy: #123f86;
    --brand-blue: #1a5ea6;
    --accent-blue: #2f7fd0;
    --band: rgba(48, 48, 50, 0.82);
    --paper: #f1f1f1;
    --paper-shade: #e2e2e2;
    --ink: #2b2d31;
    --charcoal: #383b40;
    --white: #ffffff;
    --pale: #e6e9ef;
  }
  * { box-sizing: border-box; margin: 0; padding: 0; }
  html, body { width: 1200px; height: 576px; overflow: hidden; }
  body {
    background: var(--backdrop);
    position: relative;
    font-family: "Open Sans", sans-serif;
  }
  .card {
    position: absolute;
    top: 138px;
    border-radius: 13px;
    overflow: hidden;
    box-shadow: 0 4px 8px rgba(0,0,0,0.25);
  }

  /* Front */
  .card-front { left: 82px; width: 485px; height: 294px; }
  .front-photo {
    position: absolute; inset: 0;
    background:
      radial-gradient(ellipse at 70% 55%, rgba(60,110,180,0.55), transparent 60%),
      linear-gradient(180deg, var(--navy-deep) 0%, var(--navy) 55%, #0f3576 100%);
  }
  .front-wordmark {
    position: absolute; left: 0; right: 0; top: 78px;
    text-align: center;
    font-family: "Oxanium", sans-serif;
    font-weight: 700;
    font-size: 46px;
    color: var(--white);
    letter-spacing: 0.5px;
  }
  .services-band {
    position: absolute; left: 0; right: 0; top: 188px; height: 53px;
    background: var(--band);
    display: flex; flex-direction: column; justify-content: center; align-items: center;
    gap: 2px;
  }
  .services-line {
    font-family: "Oxanium", sans-serif;
    font-weight: 600;
    font-size: 16px;
    color: var(--pale);
    line-height: 20px;
    white-space: nowrap;
  }
  .services-line .sep { color: var(--accent-blue); margin: 0 7px; }
  .front-url {
    position: absolute; left: 0; right: 0; top: 264px;
    text-align: center;
    font-size: 12.5px;
    color: var(--pale);
  }

  /* Back */
  .card-back {
    left: 602px; width: 480px; height: 292px;
    background: linear-gradient(160deg, var(--paper) 0%, var(--paper-shade) 100%);
  }
  .back-wordmark {
    position: absolute; left: 36px; top: 120px;
    font-family: "Oxanium", sans-serif;
    font-weight: 700;
    font-size: 34px;
    color: var(--brand-blue);
  }
  .person { position: absolute; left: 286px; top: 88px; }
  .person-name {
    font-family: "Oxanium", sans-serif;
    font-weight: 700;
    font-size: 21px;
    color: var(--brand-blue);
    line-height: 26px;
  }
  .person-role { font-size: 13px; color: var(--ink); line-height: 18px; }
  .contacts { position: absolute; left: 286px; top: 146px; list-style: none; }
  .contacts li {
    display: flex; align-items: center;
    height: 18px; font-size: 13px; color: var(--ink);
  }
  .contacts svg { width: 11px; height: 11px; margin-right: 13px; fill: var(--brand-blue); }
  .contacts .highlight { color: var(--brand-blue); }
  .footer-bar { position: absolute; left: 0; bottom: 0; width: 480px; height: 38px; }
  .tagline {
    position: absolute; right: 29px; bottom: 11px;
    font-size: 13px; color: var(--white); white-space: nowrap;
  }
  .tagline .pipe { margin: 0 5px; }
</style>
</head>
<body>

<section class="card card-front">
  <div class="front-photo" role="img" aria-label="Photo of a rope access technician working at height over a city, tinted deep blue"></div>
  <div class="front-wordmark">Quarry Vale</div>
  <div class="services-band">
    <p class="services-line">Rope Access<span class="sep">•</span>Anchor Points<span class="sep">•</span>PPE Certification</p>
    <p class="services-line">Confined Space<span class="sep">•</span>Safety Systems<span class="sep">•</span>Rigging</p>
  </div>
  <div class="front-url">www.quarryvale.co.nz</div>
</section>

<section class="card card-back">
  <div class="back-wordmark">Quarry Vale</div>
  <div class="person">
    <p class="person-name">Reggie Stanton</p>
    <p class="person-role">Director</p>
  </div>
  <ul class="contacts">
    <li>
      <svg viewBox="0 0 12 12" aria-hidden="true"><path d="M1 4c0-1.5 2-2.5 5-2.5S11 2.5 11 4v1H8.5V3.8H3.5V5H1z M2.5 6h7l1 4.5h-9z"/></svg>
      027 816 4920
    </li>
    <li>
      <svg viewBox="0 0 12 12" aria-hidden="true"><path d="M1 2.5h10v7H1z M1.6 3l4.4 3.6L10.4 3" stroke="#f1f1f1" stroke-width="0.9"/></svg>
      reggie@quarryvale.co.nz
    </li>
    <li>
      <svg viewBox="0 0 12 12" aria-hidden="true"><circle cx="6" cy="6" r="5"/><path d="M1 6h10M6 1c-2.5 2.8-2.5 7.2 0 10M6 1c2.5 2.8 2.5 7.2 0 10" stroke="#f1f1f1" stroke-width="0.8" fill="none"/></svg>
      www.<span class="highlight">quarryvale</span>.co.nz
    </li>
  </ul>
  <svg class="footer-bar" viewBox="0 0 480 38" preserveAspectRatio="none" aria-hidden="true">
    <defs>
      <linearGradient id="footerBlue" x1="0" x2="1" y1="0" y2="0">
        <stop offset="0" stop-color="#0f3a80"/>
        <stop offset="0.5" stop-color="#1a5ea6"/>
        <stop offset="1" stop-color="#0d2c66"/>
      </linearGradient>
    </defs>
    <rect x="0" y="26" width="480" height="12" fill="var(--charcoal)"/>
    <path d="M205 38 C216 30 220 4 232 1 L480 1 L480 38 Z" fill="url(#footerBlue)"/>
  </svg>
  <p class="tagline">Safety<span class="pipe">|</span>Compliant<span class="pipe">|</span>Satisfaction</p>
</section>

</body>
</html>
```